All Natural Raw Honey & Goats Milk Body Wash Labels

We have launched a new product line of all natural Raw Honey & Goats Milk body wash with the business name being Dawn Meadow and the tag line Naturally . Their are currently three line items requiring three labels. Natural (Unscented), Japanese Honeysuckle and Caribbean.
It is a family orientated product that we want to promote as being all natural, healthy and trustworthy. It is an all Australian made product that uses our very own award winning raw honey
I can supply the file for the business name/logo upon request

Target Market(s)

Families

Industry/Entity Type

Bath & body

Requirements
Must have
• a Lux high end feel
Nice to have
• simple easy to read with minimal images
Should not have
• No cartoons

```html
<!DOCTYPE html>
<html lang="en">
<head>
<meta charset="utf-8">
<title>Dawn Meadow Body Wash Label Options</title>
<link href="https://fonts.googleapis.com/css2?family=Libre+Baskerville&family=Montserrat:wght@400;500&family=Dancing+Script:wght@500&display=swap" rel="stylesheet">
<style>
  :root {
    --backdrop: #b9b9b9;
    --label: #ffffff;
    --ink: #1f1f1f;
    --copper: #9a6a55;
    --gold: #c89b2e;
    --gold-light: #e8c766;
    --caption: #5a5a5a;
    --art: #e4e4e4;
  }
  * { margin: 0; padding: 0; box-sizing: border-box; }
  html, body { width: 1200px; height: 1200px; overflow: hidden; }
  body {
    background: var(--backdrop);
    position: relative;
    font-family: "Montserrat", sans-serif;
  }
  .label {
    position: absolute;
    top: 330px;
    width: 380px;
    height: 620px;
    background: var(--label);
    border-radius: 28px;
    text-align: center;
    color: var(--ink);
  }
  .label--one { left: 143px; }
  .label--two { left: 677px; }
  .gold-frame {
    position: absolute;
    inset: 96px 24px 64px;
    border: 2px solid var(--gold);
  }
  .content {
    position: absolute;
    left: 0; right: 0;
    top: 120px;
  }
  .brand {
    font-family: "Libre Baskerville", serif;
    font-size: 22px;
    color: var(--ink);
    display: inline-flex;
    align-items: center;
    gap: 8px;
  }
  .brand-dot {
    width: 10px; height: 10px; border-radius: 50%;
    background: var(--ink);
  }
  .claim {
    font-family: "Dancing Script", cursive;
    font-size: 19px;
    margin-top: 16px;
    margin-left: -120px;
  }
  .product-name {
    font-family: "Libre Baskerville", serif;
    font-size: 28px;
    line-height: 1.15;
    color: var(--copper);
    letter-spacing: 0.5px;
    margin-top: 4px;
  }
  .label--two .product-name { font-size: 25px; }
  .product-type {
    font-size: 18px;
    letter-spacing: 1px;
    margin-top: 16px;
  }
  .label--two .product-type { font-size: 16px; }
  .emblem {
    width: 100px; height: 100px;
    border-radius: 50%;
    border: 1.5px solid var(--ink);
    background: var(--art);
    margin: 26px auto 0;
  }
  .label--two .emblem { width: 86px; height: 86px; }
  .scent {
    width: 220px;
    margin: 34px auto 0;
    padding: 10px 0;
    border-top: 2px solid var(--ink);
    border-bottom: 2px solid var(--ink);
    font-size: 15px;
    letter-spacing: 0.6px;
  }
  .label--two .scent {
    width: 190px;
    font-size: 13px;
    margin-top: 28px;
    border-color: var(--gold);
  }
  .volume {
    font-size: 10px;
    margin-top: 26px;
  }
  .caption {
    position: absolute;
    top: 1052px;
    width: 380px;
    text-align: center;
    font-family: "Montserrat", sans-serif;
    font-size: 30px;
    color: var(--caption);
  }
  .caption--one { left: 143px; }
  .caption--two { left: 677px; }
</style>
</head>
<body>
  <section class="label label--one">
    <div class="content">
      <div class="brand"><span class="brand-dot"></span>Dawn Meadow</div>
      <p class="claim">All Natural</p>
      <h1 class="product-name">RAW HONEY &amp;<br>GOATS MILK</h1>
      <p class="product-type">BODY WASH</p>
      <div class="emblem" role="img" aria-label="Line drawing of a goat with a bee inside a circle"></div>
      <p class="scent">JAPANESE HONEYSUCKLE</p>
      <p class="volume">750ml • 26fl.oz</p>
    </div>
  </section>

  <section class="label label--two">
    <div class="gold-frame"></div>
    <div class="content">
      <div class="brand"><span class="brand-dot"></span>Dawn Meadow</div>
      <p class="claim">All Natural</p>
      <h1 class="product-name">RAW HONEY &amp;<br>GOATS MILK</h1>
      <p class="product-type">BODY WASH</p>
      <div class="emblem" role="img" aria-label="Line drawing of a goat with a bee inside a circle"></div>
      <p class="scent">JAPANESE HONEYSUCKLE</p>
      <p class="volume">750ml • 26fl.oz</p>
    </div>
  </section>

  <p class="caption caption--one">Option 1</p>
  <p class="caption caption--two">Option 2</p>
</body>
</html>
```